Commercial Construction Interior Fitout company needs Logo and Business Cards

We need a logo and business card design. We specialise in Commercial Ceilings, Partitions, Plastering and Carpentry.

Company name: 7QX Commercial Interiors. Would like a professional looking card more than a fancy look. Gloss front preferably black pattern with Fluro Green and white text.

Will need:

Name
Position
Phone
Fax
Email
Postal Address
Web address
Updates

Thank you so much everyone for your efforts and fantastic designs..   If I didn't respond to everyone personally,  my apologises. 

Again, thanks all

R.M                               

Target Market(s)

Existing & New clients in the Construction Industry

Industry/Entity Type

Business

Requirements
Nice to have
• 7QX to be overlapped or made into some sort of Logo

```html
<!DOCTYPE html>
<html lang="en">
<head>
<meta charset="utf-8">
<title>7QX Commercial Interiors – Business Card</title>
<link rel="stylesheet" href="https://fonts.googleapis.com/css2?family=Open+Sans:wght@400;700&display=swap">
<style>
  :root {
    --page-bg: #e9e9e6;
    --card-dark: #232323;
    --card-dark-edge: #151515;
    --fluro-green: #97c93d;
    --text-white: #ffffff;
    --shadow: rgba(0, 0, 0, 0.35);
  }
  * { box-sizing: border-box; margin: 0; padding: 0; }
  html, body {
    width: 1200px; height: 1000px; overflow: hidden;
    background: var(--page-bg);
    font-family: "Open Sans", Arial, sans-serif;
  }
  .canvas { position: relative; width: 1200px; height: 1000px; }

  .card {
    position: absolute;
    width: 750px; height: 460px;
    background: radial-gradient(ellipse at 50% 40%, var(--card-dark) 0%, var(--card-dark-edge) 100%);
    box-shadow: 0 10px 30px var(--shadow);
    overflow: hidden;
  }
  .card--front { left: 60px; top: 60px; z-index: 2; }
  .card--back { left: 390px; top: 470px; z-index: 1; }

  .torn-bands { position: absolute; inset: 0; width: 100%; height: 100%; }

  .wordmark {
    position: absolute;
    font-weight: 700;
    text-transform: uppercase;
    display: flex; align-items: center; gap: 12px;
  }
  .wordmark__square { width: 18px; height: 18px; flex: none; }
  .wordmark--front {
    left: 70px; top: 200px; width: 330px;
    color: var(--text-white); font-size: 30px; line-height: 1.15;
  }
  .wordmark--front .wordmark__square { background: var(--text-white); }
  .wordmark--back {
    left: 70px; top: 190px;
    color: var(--fluro-green); font-size: 40px; letter-spacing: 1px;
  }
  .wordmark--back .wordmark__square { background: var(--fluro-green); width: 24px; height: 24px; }

  .contact { position: absolute; left: 455px; top: 160px; color: var(--text-white); }
  .contact__name { font-size: 22px; font-weight: 400; letter-spacing: 0.5px; }
  .contact__position { font-size: 13px; color: var(--fluro-green); margin-top: 2px; text-transform: uppercase; }
  .contact__list { list-style: none; margin-top: 22px; }
  .contact__item {
    display: flex; align-items: center; gap: 12px;
    font-size: 13.5px; margin-bottom: 9px;
  }
  .contact__icon { width: 14px; height: 14px; flex: none; }
</style>
</head>
<body>
<main class="canvas">

  <section class="card card--front" aria-label="Business card front">
    <svg class="torn-bands" viewBox="0 0 750 460" preserveAspectRatio="none" aria-hidden="true">
      <polygon fill="var(--fluro-green)" points="0,0 750,0 750,78 735,82 722,76 706,86 690,80 672,88 655,84 640,92 622,86 604,95 588,90 570,97 552,93 536,100 518,96 500,104 482,99 466,106 450,102 432,110 414,105 398,113 380,108 362,116 345,111 328,119 310,114 292,122 275,118 258,126 240,121 222,129 205,124 188,133 170,128 152,136 135,131 118,139 100,134 82,142 66,137 48,145 30,140 14,147 0,143"/>
      <polygon fill="var(--fluro-green)" points="0,460 750,460 750,340 734,336 718,344 700,338 684,346 666,341 650,349 632,344 614,352 598,348 580,356 562,351 546,359 528,354 510,362 494,357 476,366 458,361 442,368 424,364 406,372 390,367 372,375 354,370 338,378 320,373 302,381 286,376 268,384 250,380 234,388 216,383 198,391 182,386 164,394 146,389 130,397 112,392 94,400 78,396 60,403 42,399 26,406 0,402"/>
    </svg>

    <div class="wordmark wordmark--front">
      <span class="wordmark__square"></span>
      <span>7QX Commercial Interiors</span>
    </div>

    <div class="contact">
      <h1 class="contact__name">NAME HERE</h1>
      <p class="contact__position">Position</p>
      <ul class="contact__list">
        <li class="contact__item">
          <svg class="contact__icon" viewBox="0 0 14 14" aria-hidden="true"><path fill="var(--fluro-green)" d="M7 0a5 5 0 0 0-5 5c0 3.6 5 9 5 9s5-5.4 5-9a5 5 0 0 0-5-5zm0 7a2 2 0 1 1 0-4 2 2 0 0 1 0 4z"/></svg>
          POSTAL ADDRESS TYPE HERE
        </li>
        <li class="contact__item">
          <svg class="contact__icon" viewBox="0 0 14 14" aria-hidden="true"><path fill="var(--fluro-green)" d="M1 4c0-1.5 2.5-2.5 6-2.5S13 2.5 13 4v1.5h-3V4.2H4v1.3H1zM3 7h8l1.5 5.5h-11z"/><circle cx="7" cy="9.5" r="1.4" fill="var(--card-dark)"/></svg>
          000000000
        </li>
        <li class="contact__item">
          <svg class="contact__icon" viewBox="0 0 14 14" aria-hidden="true"><rect x="0.5" y="2.5" width="13" height="9" fill="var(--fluro-green)"/><path d="M0.5 2.5l6.5 5 6.5-5" fill="none" stroke="var(--card-dark)" stroke-width="1.2"/></svg>
          EMAIL@MAILBOX.COM
        </li>
        <li class="contact__item">
          <svg class="contact__icon" viewBox="0 0 14 14" aria-hidden="true"><g fill="none" stroke="var(--fluro-green)" stroke-width="1.3"><circle cx="7" cy="7" r="6"/><ellipse cx="7" cy="7" rx="2.6" ry="6"/><path d="M1 7h12M2 4h10M2 10h10"/></g></svg>
          www.WEBADDRESS.com
        </li>
      </ul>
    </div>
  </section>

  <section class="card card--back" aria-label="Business card back">
    <div class="wordmark wordmark--back">
      <span class="wordmark__square"></span>
      <span>7QX Commercial Interiors</span>
    </div>
  </section>

</main>
</body>
</html>
```